Exciting & Elegant Stationary Pack

Stationary consists of
1. Letter head / Envelope
2. Business Card
3. Invoice
4. 40x40mm sticker

Attached files;

1. Logo (Other formats available on request)
2. MS word Doc - For information and description of design
3. Website image (This will be our new website so use the colours so everything ties together)
4. Sample of stationary pack we like, but feel free to be creative

Target Market(s)

Home improvement

Industry/Entity Type

Construction

Font styles to use
Other font styles liked:
• Leave up to designer - We like font used on (website attached image)

Requirements
Must have
• Please look at uploaded file of sample website and use colours
Nice to have
• Any type of business card design - eg. metal, die cut, embossed, etc...

```html
<!DOCTYPE html>
<html lang="en">
<head>
<meta charset="utf-8">
<title>Groutwell Tiling – Stationery Pack</title>
<link href="https://fonts.googleapis.com/css2?family=Lato:wght@400;700;900&display=swap" rel="stylesheet">
<style>
:root{
  --navy:#1e4a72;
  --navy-faint:#2a5680;
  --red:#c8333a;
  --paper:#f2f2f2;
  --backdrop:#d3d3d3;
  --ink:#333;
  --muted:#777;
}
*{box-sizing:border-box;margin:0;padding:0}
html,body{width:1200px;height:857px;overflow:hidden}
body{background:var(--backdrop);font-family:'Lato',sans-serif;color:var(--ink);position:relative}
.piece{position:absolute;background:var(--paper);overflow:hidden}
.brand{display:flex;align-items:center;gap:5px;font-weight:900;color:var(--navy);letter-spacing:.5px;white-space:nowrap}
.brand .mark{background:var(--navy);display:inline-block}
.brand.on-dark{color:#fff}
.brand.on-dark .mark{background:#fff}
.band{position:absolute;left:0;bottom:0;display:block}

/* cover sheet */
.cover{left:67px;top:33px;width:370px;height:482px}
.cover .brand{position:absolute;left:88px;top:86px;font-size:26px}
.cover .brand .mark{width:16px;height:16px}
.cover .stripe{position:absolute;left:0;top:150px;width:100%;height:9px;background:var(--red)}
.cover .field{position:absolute;left:0;top:165px;width:100%;bottom:0;background:var(--navy)}
.cover .ghost{position:absolute;left:0;right:0;top:120px;text-align:center;font-weight:900;font-size:58px;color:var(--navy-faint);letter-spacing:2px}

/* letterhead */
.letterhead{left:465px;top:50px;width:358px;height:465px}
.letterhead .brand{position:absolute;left:32px;top:20px;font-size:13px}
.letterhead .brand .mark{width:9px;height:9px}
.letter-body{position:absolute;left:35px;top:122px;width:290px;font-size:6.2px;line-height:1.65;text-align:justify}
.letter-body p{margin-bottom:7px}
.signature{display:block;width:110px;height:26px;margin-top:14px;background:linear-gradient(90deg,#e4e4e4,#d8d8d8)}
.sign-role{font-size:6.5px;margin-top:6px}
.letter-contact{position:absolute;left:40px;bottom:28px;font-size:6px;color:var(--navy);line-height:1.6}
.letter-contact strong{font-size:7px}
.abn{position:absolute;font-weight:700;color:var(--red);font-size:7px}
.abn span{color:var(--navy)}
.letterhead .abn{right:36px;bottom:25px}

/* invoice */
.invoice{left:849px;top:50px;width:330px;height:465px}
.invoice .brand{position:absolute;left:22px;top:14px;font-size:11px}
.invoice .brand .mark{width:8px;height:8px}
.inv-row{position:absolute;left:26px;right:26px;display:flex;justify-content:space-between;font-size:6px;color:var(--navy)}
.inv-row em{font-style:normal;color:var(--red)}
.inv-meta{top:62px}
.inv-to{top:82px;border-top:1px solid var(--navy);padding-top:5px}
.inv-table{position:absolute;left:22px;top:148px;width:285px;border-collapse:collapse;font-size:5px}
.inv-table th,.inv-table td{border:.6px solid #444;height:7px;padding:0 2px}
.inv-table th{background:#ddd;font-weight:700}
.inv-table td.num{text-align:right}
.inv-totals{position:absolute;left:159px;top:350px;width:148px;border-collapse:collapse;font-size:5px;font-weight:700}
.inv-totals td{border:.6px solid #444;height:14px;padding:0 3px}
.inv-contact{position:absolute;left:22px;bottom:18px;font-size:4.6px;color:var(--navy);line-height:1.5}
.invoice .abn{right:55px;bottom:27px;font-size:5px}

/* envelope front */
.env-front{left:33px;top:538px;width:404px;height:175px}
.env-front .brand{position:absolute;left:18px;top:14px;font-size:12px}
.env-front .brand .mark{width:8px;height:8px}
.env-front .addr{position:absolute;left:18px;bottom:14px;font-size:5.5px;color:var(--navy)}
.env-front .abn{right:12px;bottom:19px}

/* envelope back */
.env-back{left:465px;top:538px;width:408px;height:175px}
.env-back .brand{position:absolute;left:0;right:0;top:14px;justify-content:center;font-size:15px;color:#8a9bb0}
.env-back .brand .mark{width:10px;height:10px;background:#8a9bb0}

/* business cards */
.card-front{left:285px;top:737px;width:152px;height:86px;background:var(--navy)}
.card-front .brand{position:absolute;left:0;right:0;top:24px;justify-content:center;font-size:16px}
.card-front .brand .mark{width:10px;height:10px}
.card-front .url{position:absolute;left:0;right:0;bottom:12px;text-align:center;font-size:5px;color:#fff;font-weight:700}
.card-back{left:465px;top:737px;width:150px;height:86px}
.card-back .brand{position:absolute;right:10px;top:10px;font-size:9px}
.card-back .brand .mark{width:6px;height:6px}
.card-back .person{position:absolute;left:10px;top:49px;font-size:4.3px;line-height:1.45;color:var(--muted)}
.card-back .person b{color:var(--red);font-weight:700}
.card-back .licence{position:absolute;right:14px;bottom:2px;font-size:5px;color:#fff}

/* sticker */
.sticker{position:absolute;left:900px;top:602px;width:254px;height:254px;border-radius:50%;background:var(--navy);display:flex;flex-direction:column;align-items:center;justify-content:center;color:#fff;text-align:center}
.sticker::before{content:"";position:absolute;inset:9px;border:2px solid #fff;border-radius:50%}
.sticker .brand{font-size:27px}
.sticker .brand .mark{width:16px;height:16px}
.sticker .st-addr{font-size:13px;line-height:1.35;margin-top:22px}
.sticker .st-phone{font-size:17px;font-weight:700;margin-top:12px;letter-spacing:.5px}
</style>
</head>
<body>

<section class="piece cover">
  <div class="brand"><span class="mark"></span>GROUTWELL</div>
  <div class="stripe"></div>
  <div class="field"><div class="ghost">GROUTWELL<br>TILING</div></div>
</section>

<section class="piece letterhead">
  <div class="brand"><span class="mark"></span>GROUTWELL</div>
  <div class="letter-body">
    <p>Dear Client</p>
    <p>Lorem ipsum dolor sit amet, consectetur adipiscing elit. Pellentesque semper purus ornare dolor eleifend aliquam. Integer molestie gravida sem a porttitor. Quisque pulvinar tellus ut ipsum molestie ultricies id non turpis. Phasellus feugiat ornare feugiat. Integer nec velit eu justo laoreet condimentum. Aenean non commodo quam. Phasellus lacinia aliquet turpis. Praesent non elit nec ante porta cursus. Morbi et augue enim, nec ultrices augue. Etiam tempus arcu laoreet metus tristique ultrices.</p>
    <p>Curabitur nec venenatis risus. Integer nec nisi sit amet leo mattis aliquam. Vivamus vulputate tellus quis purus lobortis rutrum. Aenean nec ipsum ut mauris faucibus facilisis vel porttitor neque. Morbi molestie magna id neque scelerisque ut iaculis justo porttitor. Sed est ligula, semper at cursus ac, porttitor ac ipsum. Maecenas pulvinar euismod tempor. Pellentesque habitant morbi tristique senectus et netus et malesuada fames ac turpis egestas. Integer nec velit turpis. Aliquam adipiscing massa sed ipsum commodo id ullamcorper leo volutpat. Sed vitae tellus dui.</p>
    <p>Maecenas vel neque ante, id faucibus ipsum. Suspendisse non neque quis nunc rhoncus bibendum. Fusce sit amet quam quis libero facilisis ultrices. Donec dignissim lorem vel sem sodales mollis. Duis nec sem lorem, at tristique nibh. In rutrum fermentum lectus, nec dictum leo tincidunt in. Nam metus odio, molestie a tempor a, laoreet placerat dui. Fusce sit amet nisi at elit bibendum imperdiet. Sed fringilla nisi non nunc facilisis in ullamcorper justo suscipit. Fusce fermentum tincidunt sagittis.</p>
    <span class="signature" role="img" aria-label="Handwritten signature of the managing director"></span>
    <div class="sign-role">Managing Director</div>
  </div>
  <div class="letter-contact">PO BOX 48 BROOKVALE NSW 2100<br><strong>☎ 0400 123 456</strong><br><strong>◉ www.groutwelltiling.com.au</strong></div>
  <div class="abn">ABN: <span>12 345 678 901</span></div>
  <svg class="band" width="358" height="20" viewBox="0 0 358 20"><polygon points="235,0 358,0 358,20 215,20" fill="#1e4a72"/><polygon points="0,9 222,9 212,20 0,20" fill="#c8333a"/></svg>
</section>

<section class="piece invoice">
  <div class="brand"><span class="mark"></span>GROUTWELL</div>
  <div class="inv-row inv-meta"><span>TAX INVOICE: <em>5102847</em></span><span>DATE: <em>31/08/2016</em></span></div>
  <div class="inv-row inv-to"><span>TO: <em>HARBOUR BUILD GROUP</em></span><span>SITE ADDRESS: <em>12 KENT ST PARRAMATTA</em></span></div>
  <table class="inv-table">
    <tr><th style="width:55%">DESCRIPTION</th><th>RATE</th><th>UNIT</th><th>TOTAL</th></tr>
    <tr><td>Service</td><td class="num">$1</td><td class="num">1</td><td class="num">$1.00</td></tr>
    <tr><td></td><td></td><td></td><td class="num">$0.00</td></tr>
    <tr><td></td><td></td><td></td><td class="num">$0.00</td></tr>
    <tr><td></td><td></td><td></td><td class="num">$0.00</td></tr>
    <tr><td></td><td></td><td></td><td class="num">$0.00</td></tr>
    <tr><td></td><td></td><td></td><td class="num">$0.00</td></tr>
    <tr><td></td><td></td><td></td><td class="num">$0.00</td></tr>
    <tr><td></td><td></td><td></td><td></td></tr><tr><td></td><td></td><td></td><td></td></tr>
    <tr><td></td><td></td><td></td><td></td></tr><tr><td></td><td></td><td></td><td></td></tr>
    <tr><td></td><td></td><td></td><td></td></tr><tr><td></td><td></td><td></td><td></td></tr>
    <tr><td></td><td></td><td></td><td></td></tr><tr><td></td><td></td><td></td><td></td></tr>
    <tr><td></td><td></td><td></td><td></td></tr><tr><td></td><td></td><td></td><td></td></tr>
    <tr><td></td><td></td><td></td><td></td></tr><tr><td></td><td></td><td></td><td></td></tr>
    <tr><td></td><td></td><td></td><td></td></tr><tr><td></td><td></td><td></td><td></td></tr>
  </table>
  <table class="inv-totals">
    <tr><td>SUB-TOTAL</td><td>$ - 1.00</td></tr>
    <tr><td>G.S.T 10%</td><td>$ - 0.10</td></tr>
    <tr><td>TOTAL DUE</td><td>$ - 1.10</td></tr>
  </table>
  <div class="inv-contact">PO BOX 48 BROOKVALE NSW 2100<br>☎ 0400 123 456<br>◉ www.groutwelltiling.com.au</div>
  <div class="abn">ABN: <span>12 345 678 901</span></div>
  <svg class="band" width="330" height="14" viewBox="0 0 330 14"><polygon points="218,0 330,0 330,14 202,14" fill="#1e4a72"/><polygon points="0,3 208,3 198,14 0,14" fill="#c8333a"/></svg>
</section>

<section class="piece env-front">
  <div class="brand"><span class="mark"></span>GROUTWELL</div>
  <div class="addr">PO BOX 48 BROOKVALE NSW 2100</div>
  <div class="abn">ABN: <span>12 345 678 901</span></div>
  <svg class="band" width="404" height="16" viewBox="0 0 404 16"><polygon points="226,0 404,0 404,16 214,16" fill="#1e4a72"/><polygon points="0,8 216,8 208,16 0,16" fill="#c8333a"/></svg>
</section>

<section class="piece env-back">
  <svg class="band" style="top:0;bottom:auto" width="408" height="58" viewBox="0 0 408 58"><path d="M0,0 H408 L394,42 Q389,56 374,56 H34 Q19,56 14,42 Z" fill="#1e4a72"/></svg>
  <div class="brand"><span class="mark"></span>GROUTWELL</div>
</section>

<section class="piece card-front">
  <div class="brand on-dark"><span class="mark"></span>GROUTWELL</div>
  <div class="url">www.groutwelltiling.com.au</div>
</section>

<section class="piece card-back">
  <div class="brand"><span class="mark"></span>GROUTWELL</div>
  <div class="person"><b>EMPLOYEE NAME</b><br>Project Manager<br>☎ 0400 123 456<br>✉ info@groutwelltiling.com.au<br>◉ www.groutwelltiling.com.au</div>
  <svg class="band" width="150" height="9" viewBox="0 0 150 9"><polygon points="64,0 150,0 150,9 58,9" fill="#1e4a72"/><polygon points="0,4 60,4 57,9 0,9" fill="#c8333a"/></svg>
  <div class="licence">[Licence] : 204611c</div>
</section>

<section class="sticker">
  <div class="brand on-dark"><span class="mark"></span>GROUTWELL</div>
  <div class="st-addr">PO Box 48 Brookvale<br>NSW 2100</div>
  <div class="st-phone">0400 123 456</div>
</section>

</body>
</html>
```